依頼詳細
PCとスマホデザインの両方納品をいただきますが、
まずはデザインイメージが確認しやすいPCページのみの提案をお願いします。
スマホページは当選者に納品時にお願いしたいと思います。
スマホサイズは横幅750pxのサイズで作成してください。
(Lumexaディスプレイに対応するため)
レスポンシブウェブデザインを意識したデザインでお願いします。

■サイトマップ
添付の画面遷移図をご確認ください。

■参考サイト
https://kelparoute.com/
https://mivolune.jp/sportsevent/

■内容について
建築工務店が開催するイベント情報を掲載・告知をするサイトになります。
開催するイベント内容は添付のチラシのような内容の予定です。

■素材写真
画像データについては、フリー素材から流用して
イメージ画像に当て込んでください。
足りない場合は、一旦他のサイトの写真をサンプルとして
入れてください。(サンプルなどの表記をお願いします)
また、購入が必要な写真などを利用した場合、
価格とサイト名を教えてください。

また、Velmora Stockで定期契約をしていますので、
Velmora Stockの画像は使用できます。
デザイン時はカンプ画像をお入れいただきますようお願いします。

■ワイヤーフレーム
https://wire.pelvrin.com/view/a7392cdd-1148-4f0b-9d3e-e84521b07f3a-d318/
コンテンツの構成としてワイヤーフレームを作成しましたが
必ずしもワイヤーフレームの通りではなくて大丈夫です。
TOPページに配置するコンテンツを見ていただき、デザインは
デザイナーの皆様におまかせしたいと思います。

----------------------------------------------------------------------------
【制作物に対するお願い】

■サイズについて
TOPデザイン自体のアートボードサイズは、
横幅1366px、コンテンツ幅は1000pxでお願いします。
(縦幅の制限はございません)

■フォントについて
・無料で使えるフォントで作成をお願いします。
・OSに紐づくフォントの使用は控えていただければと思います (ヒラギノなど)

サイトURL
ページ数
1ページ
希望イメージ
シンプル 複雑
単色 カラフル
暗い 明るい
日常 高級
遊び心 厳粛
未来的 伝統的
女性的 男性的
希望する色
ベースカラー:白、緑 ポイントカラー:オレンジ
納品ファイル
• イラストレーター形式 (.ai)
• フォトショップ形式 (.psd)
補足説明
上記のいずれか1つ(アウトラインありとなしの2つ)と高解像度JPGを納品お願いします。
ロゴデータを追加で添付しました。

```html
<!DOCTYPE html>
<html lang="ja">
<head>
<meta charset="utf-8">
<title>緑川工務店 イベント情報</title>
<link href="https://fonts.googleapis.com/css2?family=Noto+Sans+JP:wght@400;500;700;900&family=Noto+Serif+JP:wght@500;700&display=swap" rel="stylesheet">
<style>
:root{
  --green:#3a9a2a;
  --green-deep:#2c6e2a;
  --green-dark:#1f4a24;
  --green-pale:#e9f4e4;
  --green-mist:#f2f8ef;
  --orange:#f07a12;
  --orange-deep:#e55e00;
  --ink:#333;
  --ink-soft:#666;
  --line:#cfcfcf;
  --white:#fff;
}
*{box-sizing:border-box;margin:0;padding:0}
html,body{width:1200px;height:3556px;overflow:hidden}
body{font-family:"Noto Sans JP",sans-serif;color:var(--ink);background:var(--white);position:relative}
a{text-decoration:none}
.header-brand{position:absolute;left:0;top:0;width:110px;height:50px;background:var(--white);display:flex;align-items:center;gap:8px;padding-left:10px;z-index:3}
.header-brand .mark{width:16px;height:16px;background:var(--ink)}
.header-brand span{font-weight:700;font-size:15px;letter-spacing:.05em}
.header-links{position:absolute;right:0;top:0;width:180px;height:50px;background:var(--green-deep);display:flex;align-items:center;justify-content:center;gap:26px;z-index:3}
.header-links i{width:18px;height:18px;border-radius:50%;border:2px solid var(--white)}
.hero{position:absolute;left:0;top:0;width:1200px;height:660px;
  background:linear-gradient(180deg,#cfe0ee 0%,#e7eef3 40%,#b9c5cf 70%,#8fa3a8 100%)}
.hero-photo{position:absolute;inset:0;background:radial-gradient(ellipse 520px 300px at 50% 55%,#d9dde0 0%,rgba(217,221,224,0) 70%),linear-gradient(180deg,rgba(255,255,255,0) 60%,rgba(110,140,100,.5) 100%)}
.hero-inner{position:absolute;left:0;right:0;top:95px;text-align:center}
.hero-client{display:inline-flex;align-items:center;gap:10px;font-weight:700;color:var(--green-deep);font-size:26px}
.hero-client .mark{width:22px;height:22px;background:var(--green)}
.hero-sub{font-weight:700;color:var(--orange);font-size:28px;margin-top:4px;letter-spacing:.08em}
.hero-title{font-family:"Noto Serif JP",serif;font-weight:700;font-size:118px;line-height:1.3;color:var(--orange-deep);letter-spacing:.04em;margin-top:4px;white-space:nowrap;text-shadow:0 0 12px #fff,0 0 4px #fff}
.hero-date{display:inline-block;margin-top:14px;font-weight:700;font-size:36px;color:var(--green-dark);background:rgba(255,255,255,.75);padding:2px 18px}
.btn{display:flex;align-items:center;justify-content:center;background:var(--green);color:var(--white);font-weight:500;font-size:20px;border-radius:8px;box-shadow:0 4px 0 var(--green-deep);white-space:nowrap}
.hero .btn{width:330px;height:68px;margin:40px auto 0;font-size:22px}
.side-tab{position:absolute;right:0;top:1080px;width:120px;height:250px;background:var(--green-deep);border-radius:26px 0 0 26px;color:var(--white);writing-mode:vertical-rl;display:flex;align-items:center;justify-content:center;font-size:24px;font-weight:500;line-height:1.6;letter-spacing:.2em;white-space:nowrap;z-index:4}
.events{position:absolute;left:0;top:660px;width:1200px;height:1300px;background:linear-gradient(180deg,var(--green-mist),var(--green-pale))}
.section-title{text-align:center;font-size:34px;font-weight:700;color:var(--ink);letter-spacing:.1em}
.section-title::after{content:"";display:block;width:60px;height:4px;background:var(--green);margin:14px auto 0}
.events .section-title{margin-top:62px}
.event-list{position:absolute;left:160px;top:160px;width:880px}
.event-card{display:flex;height:300px;background:var(--white);border-radius:20px;overflow:hidden;margin-bottom:22px;box-shadow:0 3px 10px rgba(0,0,0,.06)}
.event-photo{width:320px;flex:none}
.p1{background:linear-gradient(135deg,#d9dcdc,#b7bcbc)}
.p2{background:linear-gradient(135deg,#e6ddd1,#b9a58e)}
.p3{background:linear-gradient(135deg,#efece6,#c9bcae)}
.event-body{padding:44px 0 0 26px}
.event-name{color:var(--green);font-weight:700;font-size:22px;margin-bottom:22px}
.event-row{display:flex;font-size:15px;line-height:1.55;margin-bottom:16px}
.event-row dt{width:110px;padding-left:16px}
.events .btn{position:absolute;left:432px;top:1180px;width:328px;height:76px}
.news{position:absolute;left:0;top:1960px;width:1200px;height:480px}
.news .section-title{margin-top:60px}
.news-list{position:absolute;left:160px;top:130px;width:880px;border-top:1px solid var(--line);list-style:none}
.news-item{display:flex;height:60px;align-items:center;border-bottom:1px solid var(--line);font-size:15px;color:var(--ink-soft)}
.news-item time{width:120px;padding-left:6px}
.news .btn{position:absolute;left:432px;top:352px;width:328px;height:72px}
.access{position:absolute;left:0;top:2440px;width:1200px;height:680px;background:var(--green-pale)}
.access .section-title{margin-top:54px}
.access-info{position:absolute;left:40px;top:190px;width:290px}
.access-brand{display:flex;align-items:center;gap:12px;font-size:40px;font-weight:700;color:var(--green-deep);white-space:nowrap}
.access-brand .mark{width:40px;height:40px;background:var(--green)}
.access-info address{font-style:normal;font-size:16px;line-height:1.6;margin-top:20px}
.tel{display:flex;align-items:center;gap:12px;margin-top:38px;width:290px;height:84px;background:var(--green);border-radius:42px;color:var(--white);font-size:30px;font-weight:700;padding-left:24px;white-space:nowrap}
.tel svg{flex:none}
.map{position:absolute;left:340px;top:120px;width:820px;height:540px;background:linear-gradient(135deg,#eef0ec,#e2e6dc)}
.apply{position:absolute;left:0;top:3120px;width:1200px;height:436px;background:linear-gradient(90deg,#e6e1d8,#f3f0ea 50%,#cfc2ae)}
.apply-card{position:absolute;left:240px;top:40px;width:720px;height:320px;background:rgba(255,255,255,.88);border-radius:16px;text-align:center}
.apply-card h2{font-size:36px;font-weight:500;margin-top:40px;letter-spacing:.1em}
.apply-card p{font-size:17px;margin-top:18px}
.apply .btn{width:328px;height:76px;margin:40px auto 0}
</style>
</head>
<body>
<header>
  <div class="header-brand"><i class="mark"></i><span>NORVELA</span></div>
  <div class="header-links" aria-label="SNS"><i></i><i></i></div>
</header>

<section class="hero">
  <div class="hero-photo" role="img" aria-label="芝生の前庭がある白い二階建て住宅の写真"></div>
  <div class="hero-inner">
    <div class="hero-client"><i class="mark"></i>緑川工務店</div>
    <p class="hero-sub">セミナー・見学会・イベント</p>
    <h1 class="hero-title">5大イベント開催!!!</h1>
    <p class="hero-date">2021年12月19日 10時～16時</p>
    <a class="btn">お申込みはこちらから</a>
  </div>
</section>

<a class="side-tab">お申込み<br>こちらから</a>

<section class="events">
  <h2 class="section-title">最新のイベント情報</h2>
  <div class="event-list">
    <article class="event-card">
      <div class="event-photo p1" role="img" aria-label="白い壁と椅子のある明るい室内の写真"></div>
      <div class="event-body">
        <h3 class="event-name">イベント名が入ります。イベント名が入ります</h3>
        <dl>
          <div class="event-row"><dt>開催日程</dt><dd>：　2022年2月20日（木）<br>　～2022年2月24日（木）</dd></div>
          <div class="event-row"><dt>開催時間</dt><dd>：　10:00～17:00</dd></div>
          <div class="event-row"><dt>備考</dt><dd>：　テキストが入ります。テキストが入ります。</dd></div>
        </dl>
      </div>
    </article>
    <article class="event-card">
      <div class="event-photo p2" role="img" aria-label="ソファと木のテーブルがあるリビングの写真"></div>
      <div class="event-body">
        <h3 class="event-name">イベント名が入ります。イベント名が入ります</h3>
        <dl>
          <div class="event-row"><dt>開催日程</dt><dd>：　2022年2月20日（木）<br>　～2022年2月24日（木）</dd></div>
          <div class="event-row"><dt>開催時間</dt><dd>：　10:00～17:00</dd></div>
          <div class="event-row"><dt>備考</dt><dd>：　テキストが入ります。テキストが入ります。</dd></div>
        </dl>
      </div>
    </article>
    <article class="event-card">
      <div class="event-photo p3" role="img" aria-label="白いキッチンとダイニングの写真"></div>
      <div class="event-body">
        <h3 class="event-name">イベント名が入ります。イベント名が入ります</h3>
        <dl>
          <div class="event-row"><dt>開催日程</dt><dd>：　2022年2月20日（木）<br>　～2022年2月24日（木）</dd></div>
          <div class="event-row"><dt>開催時間</dt><dd>：　10:00～17:00</dd></div>
          <div class="event-row"><dt>備考</dt><dd>：　テキストが入ります。テキストが入ります。</dd></div>
        </dl>
      </div>
    </article>
  </div>
  <a class="btn">イベント情報一覧≫</a>
</section>

<section class="news">
  <h2 class="section-title">お知らせ</h2>
  <ul class="news-list">
    <li class="news-item"><time>2022.02.01</time>テキストが入ります。テキストが入ります。テキストが入ります。テキストが入ります。</li>
    <li class="news-item"><time>2022.02.01</time>テキストが入ります。テキストが入ります。テキストが入ります。テキストが入ります。</li>
    <li class="news-item"><time>2022.02.01</time>テキストが入ります。テキストが入ります。テキストが入ります。テキストが入ります。</li>
  </ul>
  <a class="btn">お知らせ一覧≫</a>
</section>

<section class="access">
  <h2 class="section-title">アクセス</h2>
  <div class="access-info">
    <div class="access-brand"><i class="mark"></i>緑川工務店</div>
    <address>〒950-0000<br>新潟県緑野市青葉町2-18<br>営業時間：8:00～18:00<br>※日曜・祝日休業</address>
    <a class="tel">
      <svg width="30" height="30" viewBox="0 0 24 24" aria-hidden="true"><path fill="#fff" d="M6.6 10.8a15 15 0 0 0 6.6 6.6l2.2-2.2c.3-.3.7-.4 1-.2 1.1.4 2.3.6 3.6.6.6 0 1 .4 1 1V20c0 .6-.4 1-1 1A17 17 0 0 1 3 4c0-.6.4-1 1-1h3.5c.6 0 1 .4 1 1 0 1.3.2 2.5.6 3.6.1.3 0 .7-.2 1z"/></svg>
      <span>0120-482-305</span>
    </a>
  </div>
  <div class="map" role="img" aria-label="店舗周辺の地図"></div>
</section>

<section class="apply">
  <div class="apply-card">
    <h2>お申込み</h2>
    <p>各イベントへのお申込みはこちらからお願いします。</p>
    <a class="btn">お申込みフォーム≫</a>
  </div>
</section>
</body>
</html>
```